Fenwick Nutrition Therapy needs a business card design

I need a business card design for my private practice. Green is my favorite color. I would like the back of the card to include an area for future appointment dates and time. I provide nutrition therapy to individuals, groups and families. I work a lot with adolescents and women who have eating disorders, but also work with athletes.
Updates

Reason: I received several new designs and would like to take some time reviewing them.

Target Market(s)

I am working primarily with women, but also men (mostly athletes). I work with a lot of runners. I work with people who are 14-60's.

Industry/Entity Type

Nutrition

Font styles to use
Serif
Sans Serif

Colors
9bcb3c
acd037

Requirements
Nice to have
• I would love to have 'Fenwick' incorporated into the design since it is my last name. If possible, I'd love to have an actual moon if it looks professional.

A picture of food could also be on the card if it is simple, but not sure how it would look with Fenwick. I am open to ideas for both Fenwick and a picture of a food item.

Other font style are fine as long as they are easy to read.

```html
<!DOCTYPE html>
<html lang="en">
<head>
<meta charset="utf-8">
<title>Fenwick Nutrition Therapy — Business Card</title>
<link rel="stylesheet" href="https://fonts.googleapis.com/css2?family=Cabin:wght@700&family=Roboto+Condensed:wght@400;700&display=swap">
<style>
  :root {
    --card-green: #9dc93b;
    --stripe-white: #ffffff;
    --band-grey: #ebeceb;
    --band-line: #d3d5d2;
    --text-grey: #6d6e70;
    --brand-ink: #5f7f1c;
    --mark-light: #efefec;
    --icon-green: #9dc93b;
    --page: #ffffff;
  }
  * { margin: 0; padding: 0; box-sizing: border-box; }
  html, body { width: 926px; height: 1200px; overflow: hidden; background: var(--page); }
  .sheet { position: relative; width: 926px; height: 1200px; }

  .card { position: absolute; left: 216px; width: 512px; background: var(--card-green); overflow: hidden; }
  .card--front { top: 226px; height: 336px; }
  .card--back { top: 648px; height: 337px; }

  .brand { position: absolute; inset: 0; }
  .brand__mark { position: absolute; border-radius: 50%; background: var(--mark-light); }
  .brand__name {
    position: absolute; font-family: "Cabin", sans-serif; font-weight: 700;
    color: var(--brand-ink); font-size: 30px; line-height: 1; white-space: nowrap;
  }

  .front-stripes { position: absolute; left: 0; right: 0; bottom: 0; height: 64px; }
  .front-stripes span { position: absolute; left: 0; right: 0; background: var(--stripe-white); }

  .contact-band {
    position: absolute; left: 0; right: 0; top: 212px; height: 76px;
    background: var(--band-grey); border-top: 1px solid var(--band-line); border-bottom: 1px solid var(--band-line);
  }
  .contact-text { position: absolute; font-family: "Roboto Condensed", sans-serif; color: var(--text-grey); white-space: nowrap; }
  .holder-name { font-size: 19px; font-weight: 700; left: 66px; top: 5px; }
  .address { left: 66px; top: 29px; font-size: 12.5px; font-weight: 700; line-height: 15px; }
  .phone { left: 370px; font-size: 13px; font-weight: 700; }
  .web-line { font-size: 13px; font-weight: 700; }
  .icon { position: absolute; }
</style>
</head>
<body>
<main class="sheet">

  <section class="card card--front" aria-label="Card front">
    <div class="brand">
      <div class="brand__mark" style="left:102px; top:112px; width:58px; height:58px;"></div>
      <div class="brand__name" style="left:172px; top:112px;">Fenwick Nutrition</div>
      <div class="brand__name" style="left:234px; top:158px;">Therapy</div>
    </div>
    <div class="front-stripes">
      <span style="top:0; height:7px;"></span>
      <span style="top:12px; height:6px;"></span>
      <span style="top:24px; height:6px;"></span>
      <span style="top:38px; height:5px;"></span>
      <span style="top:50px; height:5px;"></span>
    </div>
  </section>

  <section class="card card--back" aria-label="Card back">
    <div class="brand">
      <div class="brand__mark" style="left:30px; top:72px; width:46px; height:46px;"></div>
      <div class="brand__name" style="left:86px; top:73px; font-size:28px;">Fenwick Nutrition</div>
      <div class="brand__name" style="left:141px; top:112px; font-size:28px;">Therapy</div>
    </div>

    <div class="contact-band">
      <div class="contact-text holder-name">Dana Ellery Fenwick, MS, RD, LDN</div>

      <svg class="icon" style="left:32px; top:29px;" width="22" height="14" viewBox="0 0 22 14" aria-hidden="true">
        <rect x="0.5" y="0.5" width="21" height="13" fill="var(--icon-green)" stroke="#7fa72c"/>
        <path d="M1 1 L11 8 L21 1 M1 13 L8 6 M21 13 L14 6" fill="none" stroke="#fff" stroke-width="1.2"/>
      </svg>
      <div class="contact-text address">Postal Andress<br>4471 Maple Hollow Lane<br>Riverton, TN 37018</div>

      <svg class="icon" style="left:340px; top:30px;" width="20" height="20" viewBox="0 0 20 20" aria-hidden="true">
        <circle cx="10" cy="10" r="9.5" fill="var(--icon-green)"/>
        <path d="M6.5 5 l2 0 l1 3 l-1.5 1 a7 7 0 0 0 3 3 l1-1.5 l3 1 l0 2 a2 2 0 0 1 -2 1.5 a9 9 0 0 1 -7.5-7.5 a2 2 0 0 1 2-2.5z" fill="#fff"/>
      </svg>
      <div class="contact-text phone" style="top:32px;">555.214.3902</div>

      <svg class="icon" style="left:340px; top:52px;" width="20" height="20" viewBox="0 0 20 20" aria-hidden="true">
        <circle cx="10" cy="10" r="9.5" fill="var(--icon-green)"/>
        <rect x="5" y="8" width="10" height="6" rx="1" fill="#fff"/>
        <path d="M4.5 8 q5.5-4 11 0" fill="none" stroke="#fff" stroke-width="1.6"/>
      </svg>
      <div class="contact-text phone" style="top:55px;">555.318.8506</div>
    </div>

    <svg class="icon" style="left:32px; top:301px;" width="20" height="20" viewBox="0 0 20 20" aria-hidden="true">
      <circle cx="10" cy="10" r="8.5" fill="none" stroke="#fff" stroke-width="1.5"/>
      <ellipse cx="10" cy="10" rx="3.5" ry="8.5" fill="none" stroke="#fff" stroke-width="1.2"/>
      <path d="M2 10 H18" stroke="#fff" stroke-width="1.2"/>
    </svg>
    <div class="contact-text web-line" style="left:66px; top:302px;">www.youwebsite.com</div>

    <svg class="icon" style="left:340px; top:300px;" width="20" height="20" viewBox="0 0 20 20" aria-hidden="true">
      <path d="M1 8 L10 1 L19 8 V19 H1 Z" fill="#c9e08a" stroke="#7fa72c"/>
      <text x="10" y="16" text-anchor="middle" font-family="Arial, sans-serif" font-size="10" font-weight="700" fill="#6d6e70">@</text>
    </svg>
    <div class="contact-text web-line" style="left:368px; top:302px;">dfenwick@greenmail.net</div>
  </section>

</main>
</body>
</html>
```